Business Card Admin Services

I have just selected a new logo. Now I need a business card.

The business is contract administrative services. We provide high value administrative services to small businesses/offices. We are professional, efficient, but also have fun and energetic personalities.

Lora Pike
Lora@DeskFalcon.ca
604-913-4078
DeskFalcon.ca

I will also want Facebook, Twitter and LinkedIn icons on the card - please up my "handles" beside each.
Facebook is DeskFalconCanada
Twitter is @DFalconLora
LinkedIn is LoraPikeDeskFalcon
Updates

New logo just updated.  Thanks for your patience!

Target Market(s)

Small businesses, professional offices

Industry/Entity Type

Business

Requirements
Must have
• bold, fun use of my colours
font needs to be consistent with the logo
Nice to have
• I quite like a closeup of the head

```html
<!DOCTYPE html>
<html lang="en">
<head>
<meta charset="utf-8">
<title>Desk Falcon – Business Card</title>
<link href="https://fonts.googleapis.com/css2?family=Montserrat:wght@300;600;700&family=Open+Sans:wght@400;600&display=swap" rel="stylesheet">
<style>
  :root {
    --stage: #2b2b2b;
    --card: #161616;
    --pink: #e8087e;
    --white: #f2f2f2;
    --muted: #cfcfcf;
  }
  * { box-sizing: border-box; margin: 0; padding: 0; }
  html, body { width: 1200px; height: 900px; overflow: hidden; }
  body {
    background: var(--stage);
    font-family: "Open Sans", Arial, sans-serif;
    position: relative;
  }
  .card {
    position: absolute;
    top: 300px;
    width: 520px;
    height: 300px;
    background: var(--card);
    box-shadow: 0 14px 30px rgba(0,0,0,.55);
    overflow: hidden;
  }
  .card--front { left: 50px; }
  .card--back { left: 630px; }

  .brand {
    position: absolute;
    display: flex;
    align-items: center;
    gap: 12px;
  }
  .brand__mark {
    width: 64px; height: 64px;
    border-radius: 50%;
    background: var(--pink);
    flex: none;
  }
  .brand__name {
    font-family: "Montserrat", Arial, sans-serif;
    font-weight: 700;
    color: var(--pink);
    letter-spacing: 1px;
    white-space: nowrap;
  }
  .rule {
    position: absolute;
    height: 1px;
    background: var(--pink);
  }

  /* front */
  .card--front .brand { left: 130px; top: 92px; }
  .card--front .brand__mark { width: 86px; height: 86px; }
  .card--front .brand__name { font-size: 36px; }
  .card--front .rule--top { left: 0; top: 110px; width: 120px; }
  .card--front .rule--bottom { left: 120px; right: 0; top: 200px; }
  .website {
    position: absolute;
    left: 150px; top: 190px;
    padding: 0 8px;
    background: var(--card);
    font-family: "Montserrat", Arial, sans-serif;
    font-weight: 600;
    font-size: 12px;
    letter-spacing: 2px;
    color: var(--white);
  }
  .website__domain { color: var(--pink); }

  /* back */
  .card--back .brand { left: 150px; top: 26px; }
  .card--back .brand__name { font-size: 28px; }
  .holder {
    position: absolute;
    left: 40px; top: 104px;
    padding-right: 8px;
    background: var(--card);
    font-family: "Montserrat", Arial, sans-serif;
    font-size: 12px;
    letter-spacing: 3px;
    color: var(--white);
  }
  .holder__last { color: var(--pink); font-weight: 700; }
  .card--back .rule--name { left: 20px; right: 20px; top: 112px; }
  .contact {
    position: absolute;
    left: 40px; top: 136px;
    list-style: none;
    font-size: 10px;
    line-height: 17px;
    color: var(--muted);
  }
  .contact__label { color: var(--pink); font-weight: 600; margin-right: 4px; }
  .card--back .rule--band { left: 0; right: 0; top: 232px; }
  .social {
    position: absolute;
    right: 30px; top: 196px;
    text-align: center;
  }
  .social__title {
    font-family: "Montserrat", Arial, sans-serif;
    font-size: 8px;
    font-weight: 600;
    letter-spacing: 1px;
    color: var(--pink);
    margin-bottom: 5px;
  }
  .social__icons { display: flex; gap: 10px; justify-content: center; }
  .social__icon { width: 12px; height: 12px; background: var(--white); border-radius: 2px; }
  .band {
    position: absolute;
    left: 0; right: 0; bottom: 0;
    height: 26px;
    background: var(--pink);
  }
</style>
</head>
<body>
  <section class="card card--front">
    <div class="rule rule--top"></div>
    <div class="brand">
      <span class="brand__mark"></span>
      <span class="brand__name">DESK FALCON</span>
    </div>
    <div class="rule rule--bottom"></div>
    <p class="website">www.<span class="website__domain">DeskFalcon</span>.ca</p>
  </section>

  <section class="card card--back">
    <div class="brand">
      <span class="brand__mark"></span>
      <span class="brand__name">DESK FALCON</span>
    </div>
    <div class="rule rule--name"></div>
    <p class="holder">LORA <span class="holder__last">PIKE</span></p>
    <ul class="contact">
      <li><span class="contact__label">P:</span>604-913-4078</li>
      <li><span class="contact__label">E:</span>Lora@DeskFalcon.ca</li>
      <li><span class="contact__label">W:</span>DeskFalcon.ca</li>
    </ul>
    <div class="social">
      <p class="social__title">FOLLOW US ON :</p>
      <div class="social__icons">
        <span class="social__icon"></span>
        <span class="social__icon"></span>
        <span class="social__icon"></span>
      </div>
    </div>
    <div class="rule rule--band"></div>
    <div class="band"></div>
  </section>
</body>
</html>
```